Business cards for a high-end menswear store

I would like to come up with a design for our business cards.
Two different ones: one for general sales and one for the owner. It is a high-end menswear store.

Our address is: 4817 Morneau Boulevard, Montreal, QC, K7P4M2
phone number: 514-286-5937
insta: MAISONVERLAINE
Website: www.maisonverlaine.example
email (general card): info@maisonverlaine.example
email (owner): bastien@maisonverlaine.example

I have attached our logo in an ai and eps file format. You can see our old cards as well. I am looking for a modern and clean look.

Target Market(s)

High-End Clothing Market

Industry/Entity Type

Retail, Clothing, Luxury Clothing

Contact Information for Business Card

Address, Name, Email, Website, Social Info,

Font styles to use
Serif

Colors

Designer to choose colors to be used in the design.

Requirements
Must have
• Address, Name, Email, Website, Social Info,
Nice to have
• QR Code that brings you to the website

```html
<!DOCTYPE html>
<html lang="en">
<head>
<meta charset="utf-8">
<title>Maison Verlaine — Business Cards</title>
<link href="https://fonts.googleapis.com/css2?family=Gelasio:wght@400&display=swap" rel="stylesheet">
<style>
  :root {
    --page: #ffffff;
    --ink: #231f20;
    --paper: #ffffff;
    --accent: #2a4a8a;
    --light: #ffffff;
    --mark-back: #4a4647;
    --name-back: #bdbabb;
  }
  * { box-sizing: border-box; margin: 0; padding: 0; }
  html, body {
    width: 1200px; height: 1200px; overflow: hidden;
    background: var(--page);
    font-family: "Gelasio", Georgia, serif;
    color: var(--ink);
  }
  .sheet { position: relative; width: 1200px; height: 1200px; }

  .card {
    position: absolute; left: 212px; width: 783px; height: 458px;
    box-shadow: 0 2px 10px rgba(0,0,0,0.28);
  }
  .card--front { top: 97px; background: var(--paper); }
  .card--back  { top: 653px; background: var(--ink); }

  .brand-name {
    position: absolute; width: 200px;
    font-size: 13px; letter-spacing: 0.34em; line-height: 1;
    text-align: center; white-space: nowrap;
  }
  .brand-block { position: absolute; width: 200px; height: 200px; background: var(--ink); }

  .card--front .brand-name { left: 104px; top: 89px; color: var(--ink); }
  .card--front .brand-block { left: 104px; top: 108px; }

  .divider {
    position: absolute; left: 365px; top: 89px;
    width: 1.5px; height: 218px; background: var(--accent);
  }

  .contact-list { position: absolute; left: 418px; top: 135px; list-style: none; }
  .contact-item {
    display: flex; align-items: center;
    height: 32px; font-size: 19px; line-height: 1;
  }
  .contact-icon { width: 19px; height: 19px; margin-right: 12px; flex: none; }

  .address-band {
    position: absolute; left: 0; top: 396px; width: 100%; height: 36px;
    background: var(--ink);
    border-top: 1.5px solid var(--accent);
    border-bottom: 1.5px solid var(--accent);
    color: var(--light); font-size: 17px;
    display: flex; align-items: center; justify-content: center;
  }

  .card--back .brand-name { left: 294px; top: 122px; color: var(--name-back); font-size: 12.5px; }
  .card--back .brand-block { left: 294px; top: 141px; width: 193px; height: 193px; background: var(--mark-back); }
</style>
</head>
<body>
<main class="sheet">

  <section class="card card--front" aria-label="Business card, front">
    <div class="brand-name">MAISON VERLAINE</div>
    <div class="brand-block"></div>

    <div class="divider"></div>

    <ul class="contact-list">
      <li class="contact-item">
        <svg class="contact-icon" viewBox="0 0 24 24" aria-hidden="true">
          <path fill="#231f20" d="M6.6 2.5l3 3.6c.4.5.4 1.2 0 1.7L8 9.6c1.3 2.6 3.8 5.1 6.4 6.4l1.8-1.6c.5-.4 1.2-.4 1.7 0l3.6 3c.5.4.6 1.2.1 1.7l-1.9 2.2c-.6.6-1.5.9-2.3.6C9.9 19.7 4.3 14.1 2.1 6.6c-.3-.8 0-1.7.6-2.3l2.2-1.9c.5-.5 1.3-.4 1.7.1z"/>
        </svg>
        <span>514-286-5937</span>
      </li>
      <li class="contact-item">
        <svg class="contact-icon" viewBox="0 0 24 24" aria-hidden="true">
          <rect x="2" y="5" width="20" height="14" fill="#231f20"/>
          <path d="M2.5 5.5L12 13l9.5-7.5M2.5 18.5l7-6.5M21.5 18.5l-7-6.5" fill="none" stroke="#ffffff" stroke-width="1.4"/>
        </svg>
        <span>info@maisonverlaine.example</span>
      </li>
      <li class="contact-item">
        <svg class="contact-icon" viewBox="0 0 24 24" aria-hidden="true">
          <g fill="none" stroke="#231f20" stroke-width="1.6">
            <circle cx="12" cy="12" r="10"/>
            <ellipse cx="12" cy="12" rx="4.5" ry="10"/>
            <path d="M2 12h20M3.5 7h17M3.5 17h17"/>
          </g>
        </svg>
        <span>www.maisonverlaine.example</span>
      </li>
      <li class="contact-item">
        <svg class="contact-icon" viewBox="0 0 24 24" aria-hidden="true">
          <rect x="3" y="3" width="18" height="18" fill="none" stroke="#231f20" stroke-width="1.8"/>
        </svg>
        <span>MAISONVERLAINE</span>
      </li>
    </ul>

    <div class="address-band">4817 Morneau Boulevard, Montreal, QC, K7P4M2</div>
  </section>

  <section class="card card--back" aria-label="Business card, back">
    <div class="brand-name">MAISON VERLAINE</div>
    <div class="brand-block"></div>
  </section>

</main>
</body>
</html>
```